psd/html for a e wallet payment website designed

hi
i am in need of a psd / html for a whole website designed
the site is a e wallet /payment system i can i will provide a link to what type of style i am looking for but i can not stress this enough i do not want anyone replicating the website i am just providing the links to show you what kind of function and the content that is involved also, i have a srs with detailed pages you can read and refer to if need be
thanks of viewing
Plimvora.com
Quindrel.com
brankowelt.com
Tazurnik.com

```html
<!DOCTYPE html>
<html lang="en">
<head>
<meta charset="utf-8">
<title>Purselane – Easy Payment Method</title>
<link href="https://fonts.googleapis.com/css2?family=Open+Sans:wght@400;600;700&display=swap" rel="stylesheet">
<style>
  :root{
    --blue:#1f4f9a;
    --blue-dark:#17407f;
    --nav-top:#3068b5;
    --nav-bottom:#1b4688;
    --red:#c0391b;
    --red-light:#d8471f;
    --text:#444;
    --muted:#666;
    --band:#efefef;
    --line:#dcdcdc;
    --footer:#ebebeb;
    --base:#262626;
  }
  *{box-sizing:border-box;margin:0;padding:0}
  html,body{width:979px;height:1200px;overflow:hidden;background:#fff}
  body{position:relative;font-family:"Open Sans",Arial,sans-serif;color:var(--text)}
  .abs{position:absolute}

  /* header */
  .brand{left:81px;top:60px;display:flex;align-items:center;gap:8px}
  .brand-mark{width:34px;height:34px;border-radius:50%;background:var(--blue)}
  .brand-name{font-size:32px;font-weight:400;color:var(--blue);letter-spacing:-.5px}
  .btn{top:31px;height:27px;line-height:27px;padding:0 10px;font-size:11px;font-weight:600;color:#fff;border-radius:2px}
  .btn-register{left:768px;width:69px;background:var(--blue);text-align:center}
  .btn-login{left:840px;width:57px;background:#555;text-align:center}
  .lang{left:625px;top:76px;width:76px;height:29px;border:1px solid #ccc;font-size:11px;display:flex;align-items:center;padding-left:6px;gap:6px}
  .lang .flag{width:13px;height:9px;background:#2b3f86}
  .lang .caret{margin-left:auto;margin-right:8px;border:4px solid transparent;border-top:5px solid #333;margin-top:4px}
  .search{left:708px;top:76px;width:189px;height:29px;border:1px solid #ccc;font-size:11px;color:#444;padding:7px 12px}
  .search svg{position:absolute;right:8px;top:7px}

  /* nav */
  .nav{left:0;top:136px;width:979px;height:43px;background:linear-gradient(var(--nav-top),var(--nav-bottom))}
  .nav ul{list-style:none;display:flex;position:absolute;left:82px;top:0;height:43px;border-right:1px solid #174079}
  .nav li{height:43px;line-height:43px;color:#fff;font-size:11.5px;font-weight:600;padding:0 20px;border-left:1px solid #174079}
  .nav li.active{background:#333}

  /* hero */
  .band{left:0;top:179px;width:979px;height:347px;background:var(--band)}
  .hero{left:81px;top:190px;width:817px;height:325px;background:#e2e3e1}
  .hero-photo{position:absolute;left:0;top:0;width:400px;height:325px;background:linear-gradient(100deg,#d9d4cc,#b7a79a 45%,#dfe2e2)}
  .hero-copy{position:absolute;right:40px;top:62px;width:300px;text-align:right}
  .hero-copy h1{font-size:26px;font-weight:600;color:var(--red);margin-bottom:12px}
  .hero-copy p{font-size:12px;line-height:20.5px;color:#333}
  .know{display:inline-block;margin-top:11px;background:#fff;font-size:10.5px;color:#555;padding:6px 10px;border-radius:2px}
  .dots{position:absolute;left:731px;top:293px;display:flex;gap:8px}
  .dots span{width:11px;height:11px;border-radius:50%;background:#aaa}
  .dots span:first-child{background:#666}

  /* welcome */
  .welcome{left:90px;top:557px;width:570px}
  .welcome h2{font-size:20px;font-weight:400;color:var(--red);margin-bottom:8px}
  .welcome p{font-size:11px;line-height:18.7px;color:#555;text-align:justify}
  .wallet-photo{left:696px;top:566px;width:193px;height:111px;border-radius:8px;background:radial-gradient(ellipse at 45% 45%,#3a3a3a,#1c1c1c 60%,#fff 72%)}
  .rule{height:1px;background:var(--line)}

  /* features */
  .feature{top:732px;width:150px;text-align:center}
  .feature svg{display:block;margin:0 auto 8px}
  .feature span{font-size:15px;line-height:18.5px;color:var(--blue)}

  .partner{top:884px;font-size:16px;font-weight:700;color:#555}

  /* news */
  .news{left:701px;top:732px;width:197px;height:197px;background:var(--band)}
  .news h3{height:34px;line-height:34px;padding-left:13px;font-size:16px;font-weight:600;color:#fff;background:linear-gradient(var(--red-light),#c23416)}
  .news-item{margin:0 8px;padding:15px 0 8px 17px;border-bottom:1px solid var(--line);font-size:10.5px;line-height:16px;color:#555;position:relative}
  .news-item:last-child{border-bottom:0}
  .news-item:before{content:"";position:absolute;left:5px;top:22px;width:3px;height:3px;border-radius:50%;background:#666}
  .news-item time{display:block;color:var(--blue);margin-top:2px}

  /* footer */
  .footer{left:0;top:957px;width:979px;height:196px;background:var(--footer)}
  .footer h4{position:absolute;font-size:14px;font-weight:400;color:var(--red)}
  .links{top:1003px;list-style:none}
  .links li{font-size:11px;line-height:22px;color:#444;padding-left:10px;position:relative}
  .links li:before{content:"";position:absolute;left:0;top:10px;width:3px;height:3px;background:#666}
  .vdiv{left:701px;top:971px;width:1px;height:167px;background:#ccc}
  .social{left:721px;display:flex;align-items:center;gap:18px;font-size:10px;color:#333}
  .social i{display:block;width:22px;height:22px;border-radius:3px;background:var(--blue)}
  .social b{font-weight:400;font-size:12.5px}
  .base{left:0;top:1153px;width:979px;height:47px;background:var(--base);color:#999;font-size:11px;text-align:center;line-height:47px}
</style>
</head>
<body>

<header>
  <div class="abs brand"><span class="brand-mark"></span><span class="brand-name">Purselane</span></div>
  <a class="abs btn btn-register">REGISTER</a>
  <a class="abs btn btn-login">LOGIN</a>
  <div class="abs lang"><span class="flag"></span>Eng<span class="caret"></span></div>
  <div class="abs search">Search
    <svg width="14" height="14" viewBox="0 0 14 14"><circle cx="5.5" cy="5.5" r="4" fill="none" stroke="#222" stroke-width="2"/><line x1="8.5" y1="8.5" x2="13" y2="13" stroke="#222" stroke-width="2.5"/></svg>
  </div>
</header>

<nav class="abs nav">
  <ul>
    <li class="active">HOME</li><li>ABOUT US</li><li>HOW IT WORKS</li><li>PERSONAL ACCOUNTS</li><li>BUSINESS ACCOUNTS</li><li>SUPPORT</li><li>FAQ</li>
  </ul>
</nav>

<div class="abs band"></div>
<section class="abs hero">
  <div class="hero-photo" role="img" aria-label="Smiling couple at a laptop holding a payment card"></div>
  <div class="hero-copy">
    <h1>Easy Payment Method</h1>
    <p>Nullam pulvinar lobortis purus, a mattis urna tristique et. Donec at mi posuere, facilisis elit vel, facilisis erat. Etiam pharetra nibh eu nisi.</p>
    <span class="know">KNOW MORE</span>
  </div>
  <div class="dots"><span></span><span></span><span></span><span></span></div>
</section>

<section class="abs welcome">
  <h2>WELCOME TO PURSELANE</h2>
  <p>Aenean quis nunc fermentum, pharetra velit vitae, sodales diam. Aenean fringilla tellus sit amet pharetra aliquet. Praesent condimentum mauris ac mattis laoreet. Nullam euismod ut metus nec ultrices. Aenean conval lis odio felis. Nam vulputate mollis ante euismod venenatis. Quisque sit amet placerat ante. Phasellus ut metus eu lorem consectetur consectetur a quis leo. Cras sit amet tellus leo. Donec magna ante, congue ut nunc nec, aliquam elementum augue.</p>
</section>
<div class="abs wallet-photo" role="img" aria-label="Black leather wallet holding banknotes"></div>
<div class="abs rule" style="left:82px;top:706px;width:816px"></div>

<div class="abs feature" style="left:82px">
  <svg width="48" height="48" viewBox="0 0 48 48"><g fill="var(--blue)"><circle cx="24" cy="24" r="16"/><rect x="20" y="2" width="8" height="44"/><rect x="2" y="20" width="44" height="8"/><rect x="20" y="2" width="8" height="44" transform="rotate(45 24 24)"/><rect x="20" y="2" width="8" height="44" transform="rotate(-45 24 24)"/></g><circle cx="24" cy="24" r="9" fill="#fff"/><circle cx="24" cy="24" r="5" fill="var(--blue)"/></svg>
  <span>Easy Payment<br>Methods</span>
</div>
<div class="abs feature" style="left:235px">
  <svg width="48" height="48" viewBox="0 0 48 48"><g fill="var(--blue)"><ellipse cx="20" cy="9" rx="16" ry="6"/><rect x="4" y="13" width="32" height="9" rx="4"/><rect x="4" y="24" width="32" height="9" rx="4"/><rect x="4" y="35" width="26" height="9" rx="4"/></g><circle cx="38" cy="30" r="6" fill="#fff" stroke="var(--blue)" stroke-width="3"/><line x1="34" y1="34" x2="26" y2="44" stroke="var(--blue)" stroke-width="3"/></svg>
  <span>Date Security</span>
</div>
<div class="abs feature" style="left:388px">
  <svg width="48" height="48" viewBox="0 0 48 48"><rect x="6" y="3" width="36" height="42" rx="3" fill="var(--blue)"/><rect x="28" y="17" width="16" height="14" rx="3" fill="#fff" stroke="var(--blue)" stroke-width="2"/><circle cx="35" cy="24" r="3" fill="none" stroke="var(--blue)" stroke-width="2"/></svg>
  <span>Multiple<br>Wallets</span>
</div>
<div class="abs feature" style="left:541px">
  <svg width="60" height="48" viewBox="0 0 60 48"><rect x="20" y="2" width="38" height="30" fill="none" stroke="var(--blue)" stroke-width="4"/><rect x="30" y="36" width="18" height="4" fill="var(--blue)"/><rect x="11" y="14" width="16" height="32" fill="#fff" stroke="var(--blue)" stroke-width="4"/><rect x="2" y="26" width="11" height="20" fill="#fff" stroke="var(--blue)" stroke-width="3"/></svg>
  <span>Use Anywhere,<br>Any Device</span>
</div>
<div class="abs rule" style="left:82px;top:847px;width:604px"></div>

<div class="abs partner" style="left:106px">Tellora</div>
<div class="abs partner" style="left:213px">Vantory</div>
<div class="abs partner" style="left:336px">Brisquel</div>
<div class="abs partner" style="left:470px">Marvino</div>
<div class="abs partner" style="left:572px">Doxafire</div>

<aside class="abs news">
  <h3>Latest News</h3>
  <div class="news-item">Interdum et malesuada fames ac ante ipsum primis.<time>January 2, 2014</time></div>
  <div class="news-item">Interdum et malesuada fames ac ante ipsum primis.<time>January 2, 2014</time></div>
</aside>

<footer class="abs footer"></footer>
<h4 class="abs" style="left:92px;top:971px;font-size:14px;font-weight:400;color:var(--red)">Quick Links</h4>
<ul class="abs links" style="left:92px"><li>Integer lobortis</li><li>Curabitur ac</li><li>Phasellus tellus</li><li>Aenean fringilla</li><li>Vestibulum</li><li>Aliquam commodo</li></ul>
<ul class="abs links" style="left:245px"><li>Integer lobortis</li><li>Curabitur ac</li><li>Phasellus tellus</li><li>Aenean fringilla</li><li>Vestibulum</li><li>Aliquam commodo</li></ul>
<ul class="abs links" style="left:399px"><li>Integer lobortis</li><li>Curabitur ac</li><li>Phasellus tellus</li><li>Aenean fringilla</li><li>Vestibulum</li><li>Aliquam commodo</li></ul>
<ul class="abs links" style="left:553px"><li>Integer lobortis</li><li>Curabitur ac</li><li>Phasellus tellus</li><li>Aenean fringilla</li><li>Vestibulum</li><li>Aliquam commodo</li></ul>
<div class="abs vdiv"></div>
<h4 class="abs" style="left:721px;top:971px;font-size:14px;font-weight:400;color:var(--red)">Connect with us</h4>
<div class="abs social" style="top:1006px"><i></i><span>Join with us on <b>Chatterly</b></span></div>
<div class="abs social" style="top:1040px"><i></i><span>Follow us on <b>Quipnest</b></span></div>
<div class="abs social" style="top:1074px"><i></i><span>Share on <b>Workloop</b></span></div>
<div class="abs social" style="top:1108px"><i></i><span>Watch on <b>Viewcast</b></span></div>

<div class="abs base">Copyright &copy; 2014 &nbsp; www.purselane.com &nbsp; All rights reserved.</div>

</body>
</html>
```